shop signs for newquay all year round

We require a shop front signage
2 x 2.5m Long by 1.5m High (sides)
1 x 8m long by 0.7m High (front)

The front sign must read - £1 Max Clearance Store with the last 1.5m showing the the Xmas Shop open all year (see image 1)

The side signs must have a big bold Arrow pointing Left and one Pointing Right with the words Clearance Sale Now On (see image 2)

Colors

Designer to choose colors to be used in the design.

Requirements
Must have
• signs must be bold and clear to get shoppers into the store, it must be bright and stand out
Nice to have
• good graphics and artwork
Should not have
• plain text

```html
<!DOCTYPE html>
<html lang="en">
<head>
<meta charset="utf-8">
<title>£1 Max Clearance Store – Shop Front Signage</title>
<link rel="stylesheet" href="https://fonts.googleapis.com/css2?family=Montserrat:wght@500;600;800&display=swap">
<style>
  :root {
    --page-bg: #e6e6e6;
    --blue-edge: #3b55a0;
    --blue-mid: #2b78c9;
    --blue-arrow: #2f6fc0;
    --blue-chevron: #3a55a0;
    --xmas-sky-top: #1f4fa8;
    --xmas-sky-bottom: #5d93d8;
    --xmas-snow: #dfeaf7;
    --white: #ffffff;
  }
  * { box-sizing: border-box; margin: 0; padding: 0; }
  html, body { width: 1200px; height: 1000px; overflow: hidden; }
  body {
    position: relative;
    background: var(--page-bg);
    font-family: "Montserrat", Arial, sans-serif;
    color: var(--white);
  }
  .sign-gradient {
    background: linear-gradient(90deg, var(--blue-edge) 0%, var(--blue-mid) 35%, var(--blue-mid) 55%, var(--blue-edge) 100%);
  }

  /* Front fascia sign */
  .front-sign {
    position: absolute; left: 60px; top: 203px;
    width: 1080px; height: 137px;
    display: flex;
  }
  .front-sign__title {
    flex: 1;
    display: flex; align-items: baseline;
    padding: 30px 0 0 34px;
    font-weight: 500;
    white-space: nowrap;
  }
  .front-sign__price { font-size: 74px; letter-spacing: -1px; }
  .front-sign__max { font-size: 31px; margin: 0 22px; }
  .front-sign__name { font-size: 63px; }

  .xmas-panel {
    position: relative;
    width: 203px; height: 137px;
    background: linear-gradient(180deg, var(--xmas-sky-top) 0%, var(--xmas-sky-bottom) 75%, var(--xmas-snow) 100%);
  }
  .xmas-panel__art {
    position: absolute; left: 0; top: 40px;
    width: 84px; height: 80px;
    background: linear-gradient(180deg, rgba(223,234,247,0.35) 0%, rgba(200,70,60,0.55) 55%, rgba(223,234,247,0.6) 100%);
  }
  .xmas-panel__text {
    position: absolute; right: 18px; top: 18px;
    text-align: center; line-height: 1;
    font-weight: 800;
  }
  .xmas-panel__shop { font-size: 27px; line-height: 0.95; }
  .xmas-panel__open { font-size: 18px; margin-top: 8px; line-height: 1.05; letter-spacing: -0.3px; }

  /* Side signs */
  .side-sign {
    position: absolute; top: 366px;
    width: 475px; height: 377px;
    display: flex; flex-direction: column;
  }
  .side-sign--left { left: 60px; }
  .side-sign--right { left: 666px; }
  .side-sign__message {
    height: 267px;
    text-align: center;
    padding-top: 50px;
  }
  .side-sign__headline {
    font-weight: 800; font-size: 60px; line-height: 56px;
  }
  .side-sign__status {
    font-weight: 500; font-size: 45px; line-height: 1;
    margin-top: 28px;
  }
  .side-sign__arrow-band { height: 80px; background: var(--white); }
  .side-sign__arrow-band svg { display: block; }
  .side-sign__foot { flex: 1; }
</style>
</head>
<body>

  <header class="front-sign sign-gradient">
    <h1 class="front-sign__title">
      <span class="front-sign__price">£1</span>
      <span class="front-sign__max">Max</span>
      <span class="front-sign__name">Clearance Store</span>
    </h1>
    <div class="xmas-panel">
      <div class="xmas-panel__art" role="img" aria-label="Festive Christmas illustration on a snowy background"></div>
      <div class="xmas-panel__text">
        <div class="xmas-panel__shop">XMAS<br>SHOP</div>
        <div class="xmas-panel__open">OPEN<br>ALL YEAR</div>
      </div>
    </div>
  </header>

  <section class="side-sign side-sign--left">
    <div class="side-sign__message sign-gradient">
      <h2 class="side-sign__headline">CLEARANCE<br>SALE</h2>
      <p class="side-sign__status">NOW ON</p>
    </div>
    <div class="side-sign__arrow-band">
      <svg width="475" height="80" viewBox="0 0 475 80" aria-label="Arrow pointing left" role="img">
        <polygon points="205,8 149,40 205,72 214,72 160,40 214,8" fill="var(--blue-chevron)"/>
        <polygon points="168,40 225,9 225,29 342,29 342,56 225,56 225,71" fill="var(--blue-arrow)"/>
      </svg>
    </div>
    <div class="side-sign__foot sign-gradient"></div>
  </section>

  <section class="side-sign side-sign--right">
    <div class="side-sign__message sign-gradient">
      <h2 class="side-sign__headline">CLEARANCE<br>SALE</h2>
      <p class="side-sign__status">NOW ON</p>
    </div>
    <div class="side-sign__arrow-band">
      <svg width="475" height="80" viewBox="0 0 475 80" aria-label="Arrow pointing right" role="img">
        <polygon points="287,8 343,40 287,72 278,72 332,40 278,8" fill="var(--blue-chevron)"/>
        <polygon points="324,40 267,9 267,29 150,29 150,56 267,56 267,71" fill="var(--blue-arrow)"/>
      </svg>
    </div>
    <div class="side-sign__foot sign-gradient"></div>
  </section>

</body>
</html>
```